HPS business cards

(Generators . Lighting Towers . De-watering Pumps . Compressors) put under the logo please. my details are Owen Pritchard (Director) 0461527390 harbourpinesupply@postvale.net

```html
<!DOCTYPE html>
<html lang="en">
<head>
<meta charset="utf-8">
<title>HPS business cards</title>
<link rel="stylesheet" href="https://fonts.googleapis.com/css2?family=Nunito:wght@400;600;700;800&display=swap">
<style>
  :root {
    --backdrop: #cdcdcd;
    --card: #272726;
    --gold: #e9a630;
    --gold-deep: #c9861f;
    --white: #ffffff;
  }
  * { margin: 0; padding: 0; box-sizing: border-box; }
  html, body {
    width: 1200px; height: 1200px; overflow: hidden;
    background: var(--backdrop);
    font-family: "Nunito", sans-serif;
  }
  .card {
    position: absolute; left: 180px; width: 840px; height: 473px;
    background: var(--card); border-radius: 31px;
    box-shadow: 0 10px 30px rgba(0,0,0,0.25);
    color: var(--white);
  }
  .card--front { top: 98px; }
  .card--back { top: 628px; }

  .brand { position: absolute; left: 0; right: 0; text-align: center; color: var(--gold); font-weight: 800; }
  .brand__square { display: block; margin: 0 auto; border: 5px solid var(--gold); }
  .brand__name { display: block; letter-spacing: 1px; line-height: 1; }
  .brand__sub { display: block; letter-spacing: 12px; line-height: 1; }

  .card--front .brand { top: 152px; }
  .card--front .brand__square { width: 62px; height: 62px; margin-bottom: 22px; }
  .card--front .brand__name { font-size: 46px; }
  .card--front .brand__sub { font-size: 22px; margin-top: 10px; }

  .card--back .brand { top: 46px; }
  .card--back .brand__square { width: 40px; height: 40px; border-width: 4px; margin-bottom: 14px; }
  .card--back .brand__name { font-size: 30px; }
  .card--back .brand__sub { font-size: 15px; margin-top: 6px; letter-spacing: 8px; }

  .front-email { position: absolute; right: 32px; top: 426px; font-size: 13px; letter-spacing: 0.3px; }

  .person { position: absolute; left: 0; right: 0; top: 185px; text-align: center; }
  .person__name { font-size: 44px; font-weight: 800; letter-spacing: 3px; line-height: 1; }
  .person__role { font-size: 27px; font-weight: 600; letter-spacing: 4px; margin-top: 6px; line-height: 1; }

  .contact { position: absolute; display: flex; align-items: center; }
  .contact__icon {
    width: 39px; height: 39px; border-radius: 50%;
    background: radial-gradient(circle at 35% 30%, #f5c04d, var(--gold-deep));
    display: flex; align-items: center; justify-content: center; flex-shrink: 0;
  }
  .contact__text { font-weight: 600; line-height: 1; }
  .contact--phone { left: 286px; top: 283px; }
  .contact--phone .contact__text { font-size: 28px; letter-spacing: 5px; margin-left: 23px; }
  .contact--email { left: 143px; top: 340px; }
  .contact--email .contact__text { font-size: 27px; letter-spacing: 0.5px; margin-left: 23px; }

  .divider { position: absolute; left: 0; right: 0; top: 389px; height: 3px; background: var(--white); }
  .services { position: absolute; left: 0; right: 0; top: 410px; text-align: center; color: var(--gold); font-size: 20px; font-weight: 600; letter-spacing: 0.3px; }
</style>
</head>
<body>
  <section class="card card--front">
    <div class="brand">
      <span class="brand__square"></span>
      <span class="brand__name">HARBOUR PINE</span>
      <span class="brand__sub">SUPPLY</span>
    </div>
    <p class="front-email">harbourpinesupply@postvale.net</p>
  </section>

  <section class="card card--back">
    <div class="brand">
      <span class="brand__square"></span>
      <span class="brand__name">HARBOUR PINE</span>
      <span class="brand__sub">SUPPLY</span>
    </div>
    <div class="person">
      <p class="person__name">Pritchard</p>
      <p class="person__role">Director</p>
    </div>
    <div class="contact contact--phone">
      <span class="contact__icon">
        <svg width="20" height="20" viewBox="0 0 24 24"><path fill="#2a2a2a" d="M6.6 10.8c1.4 2.8 3.8 5.1 6.6 6.6l2.2-2.2c.3-.3.7-.4 1-.2 1.1.4 2.3.6 3.6.6.6 0 1 .4 1 1V20c0 .6-.4 1-1 1C10.6 21 3 13.4 3 4c0-.6.4-1 1-1h3.5c.6 0 1 .4 1 1 0 1.3.2 2.5.6 3.6.1.3 0 .7-.2 1l-2.3 2.2z"/></svg>
      </span>
      <span class="contact__text">0461527390</span>
    </div>
    <div class="contact contact--email">
      <span class="contact__icon">
        <svg width="22" height="16" viewBox="0 0 22 16"><rect x="1" y="1" width="20" height="14" fill="none" stroke="#2a2a2a" stroke-width="1.8"/><path d="M1 1l10 8 10-8M1 15l7-6M21 15l-7-6" fill="none" stroke="#2a2a2a" stroke-width="1.5"/></svg>
      </span>
      <span class="contact__text">harbourpinesupply@postvale.net</span>
    </div>
    <div class="divider"></div>
    <p class="services">Generators . Lighting Towers . De-watering Pumps . Compressors</p>
  </section>
</body>
</html>
```